Summit Crest Advisory - White Collar Engineering Consultancy

I'm chasing a website to provide high level information about what Summit Crest Advisory is and service's we provide - only chasing something simple. We are a new white collar secondment/contractor/professional services/consultancy specialising is providing the best consultants into contractor roles.

Our primary industries are energy, gas, pipelines, water processing, power, projects, geographic information systems, design, accounting.

Our people are mechanical,/electrical/civil/process/chemical engineers, project engineers, project managers, technical experts, GIS analysts, integrity engineers, pipeline engineers,

Currently I have this domain registered through nimbledns - https://www.scadvisoryhub.com/

I'd like to keep this domain but completely overhaul the website to be sleek and follow the logo styling.

Example websites within my industry that I like:
- https://www.bramwellfieldworks.com.au/
- https://quorvin.com.au/
- https://www.hlmtec.com.au/

I'd like the winner to code and assist with making the website functional under my domain.

Would like to include:
- industries
- services
- why work with us
- terms and conditions as per attached
- location (Brisbane)
- contact us form, that submits an email to jordan.pryce@scadvisoryhub.com
- WorkCircle link

Would definitely be looking to polish the winning result with the designer over the phone or via email.

I will also add some infrastructure photos for use; otherwise please use generic CSG related infrastructure.

Cheers,

Jordan

Industry/Entity Type

Energy, resources, gas, mining, geographic information systems, accounting, construction.

Coding

Coded - Design and coding required

Number of Pages Required

4 page

Colors
0054AA
0677BA
7BADD7
CADEEF
E8F1F8

Requirements
Must have
• Refer to project description

```html
<!DOCTYPE html>
<html lang="en">
<head>
<meta charset="utf-8">
<title>Summit Crest Advisory – White Collar Engineering Consultancy</title>
<link href="https://fonts.googleapis.com/css2?family=Montserrat:wght@400;500;600;700&family=Roboto+Condensed:wght@700&family=Lora:wght@400;500&display=swap" rel="stylesheet">
<style>
:root{
  --blue:#0054AA;
  --blue-2:#0677BA;
  --blue-3:#7BADD7;
  --blue-4:#CADEEF;
  --sky:#E8F1F8;
  --ink:#1d1d1d;
  --text:#333;
  --header:#0d0d0d;
  --white:#fff;
}
*{box-sizing:border-box;margin:0;padding:0}
html,body{width:1200px;height:4289px;overflow:hidden}
body{position:relative;font-family:"Montserrat",sans-serif;color:var(--text);background:var(--white)}
.abs{position:absolute}
.serif{font-family:"Lora",serif;font-weight:400;color:var(--blue)}
.btn{position:absolute;display:flex;align-items:center;justify-content:center;background:var(--blue);color:#fff;font-size:13px;font-weight:600}
.pill{border-radius:22px}

/* header */
.site-header{left:0;top:0;width:1200px;height:64px;background:var(--header)}
.brand{display:flex;align-items:center;gap:8px;color:#fff;font-weight:700;font-size:19px;white-space:nowrap}
.brand-dot{width:30px;height:30px;border-radius:50%;background:#fff}
.nav a{color:#fff;text-decoration:none;position:absolute;top:24px;font-size:12px}

/* hero */
.hero{left:0;top:64px;width:1200px;height:514px;background:linear-gradient(100deg,#141414 0%,#1f1f1f 40%,#2b2b2b 70%,#1a1a1a 100%)}
.hero-photo{left:664px;top:158px;width:512px;height:420px;background:linear-gradient(160deg,#8a8d90 0%,#55595d 50%,#2e3236 100%)}
.hero-sub{left:162px;top:214px;font-size:36px;font-weight:500;color:#fff;white-space:nowrap}
.hero-title{left:162px;top:260px;font-family:"Roboto Condensed",sans-serif;font-weight:700;font-size:46px;line-height:54px;color:#fff;white-space:nowrap}

/* services */
.section-title{position:absolute;left:0;width:1200px;text-align:center;font-size:40px}
.svc-icon{position:absolute;width:110px;height:110px;border-radius:50%;background:#fff;box-shadow:0 4px 14px rgba(0,0,0,.12);display:flex;align-items:center;justify-content:center}
.svc-name{position:absolute;width:300px;text-align:center;font-size:17px;font-weight:500;color:var(--ink)}
.svc-text{position:absolute;width:270px;text-align:center;font-size:12.5px;line-height:24px;color:#333}
.arrow{position:absolute;width:34px;height:34px;border-radius:50%;background:#fff;box-shadow:0 2px 8px rgba(0,0,0,.12);display:flex;align-items:center;justify-content:center;color:#888;font-size:13px}

/* about */
.band{left:0;width:1200px;background:var(--sky)}
.lead{position:absolute;left:300px;width:600px;text-align:center;font-size:12.5px;line-height:25px;color:#333}
.about-text{left:597px;top:1352px;width:445px;font-size:13px;line-height:24.5px;letter-spacing:.2px;color:#333}
.chip{position:absolute;top:1674px;height:57px;border:1px solid #9aa7b3;border-radius:4px;background:#fff;font-size:10.5px;line-height:13px;color:#555;padding:14px 0 0 16px}

/* clients */
.quote-card{position:absolute;top:2008px;width:425px;height:218px;background:#fff;box-shadow:0 3px 16px rgba(0,0,0,.09);border-bottom:4px solid var(--blue-4);text-align:center;padding-top:30px}
.quote-card h3{font-family:"Lora",serif;font-weight:500;font-size:19px;color:var(--blue)}
.quote-card p{font-size:12.5px;line-height:24.5px;margin:14px auto 0;width:380px;color:#333}

/* why */
.why-item{position:absolute;left:161px;width:381px;height:91px;background:#fff;display:flex;align-items:center;padding-left:22px;gap:24px;font-size:17px;font-weight:500;color:var(--blue)}
.why-item svg{flex:none}

/* terms */
.doc{left:0;top:3039px;width:599px;height:369px;background:#2b2b2b;padding:8px 8px 0 8px}
.doc-page{position:relative;width:583px;height:361px;background:#fff;font-size:7.4px;line-height:9.5px;color:#222;overflow:hidden}
.doc-page .c{position:absolute}
.doc-page b{font-weight:700}
.doc-bar{left:200px;top:3369px;width:200px;height:24px;border-radius:12px;background:#333;color:#fff;font-size:9px;display:flex;align-items:center;gap:12px;padding-left:14px}
.terms-title{left:681px;top:3155px;font-size:29px;font-weight:700;color:var(--blue)}
.terms-text{left:681px;top:3210px;width:370px;font-size:13.2px;line-height:27px;color:#333}

/* contact */
.contact-title{left:0;top:3490px;width:1200px;text-align:center;font-size:30px;font-weight:700;color:var(--blue)}
.field{position:absolute;left:161px;width:415px;background:#fff;border:1px solid #d8d8d8;border-radius:3px;display:flex;align-items:flex-start;padding:15px 0 0 12px;gap:14px;font-size:13px;color:#333}
.field em{color:#d0021b;font-style:normal}
.map-frame{left:623px;top:3620px;width:418px;height:356px;background:#fff;box-shadow:0 3px 14px rgba(0,0,0,.12);padding:8px}
.map{width:402px;height:340px;background:linear-gradient(135deg,#eef2ea 0%,#e4ece0 40%,#f2f0e8 70%,#e1ead9 100%)}

/* footer */
.site-footer{left:0;top:4044px;width:1200px;height:245px;background:var(--blue);color:#fff}
.foot-nav a{position:absolute;top:38px;color:#fff;font-size:12.5px;text-decoration:none}
.rule{position:absolute;left:161px;width:877px;height:1px;background:rgba(255,255,255,.3)}
.info{position:absolute;top:102px;display:flex;gap:14px;font-size:12.5px;line-height:21px}
.info .ico{width:34px;height:34px;border-radius:50%;border:1.5px solid rgba(255,255,255,.8);display:flex;align-items:center;justify-content:center;flex:none;margin-top:2px}
.info b{font-weight:600}
</style>
</head>
<body>

<!-- Header -->
<header class="abs site-header">
  <div class="abs brand" style="left:161px;top:17px"><span class="brand-dot"></span>Summit Crest Advisory</div>
  <nav class="nav">
    <a style="left:505px;font-weight:700">Home</a>
    <a style="left:592px">About Us</a>
    <a style="left:701px">Services</a>
    <a style="left:801px">Industries</a>
  </nav>
  <div class="btn" style="left:911px;top:14px;width:128px;height:37px;border-radius:2px;font-size:12px">Contact Us</div>
</header>

<!-- Hero -->
<section class="abs hero" aria-label="Introduction"></section>
<div class="abs hero-photo" role="img" aria-label="Photo of two engineers in hard hats reviewing a tablet in an industrial plant"></div>
<div class="abs hero-sub">We Are A Professionals</div>
<h1 class="abs hero-title">White Collar Engineering<br>Consultancy Business.</h1>
<div class="btn" style="left:161px;top:383px;width:127px;height:36px;border-radius:2px">Contact Us</div>

<!-- Services -->
<h2 class="section-title serif" style="top:675px">Our Services</h2>
<div class="arrow" style="left:104px;top:846px">‹</div>
<div class="arrow" style="left:1060px;top:846px">›</div>

<div class="svc-icon" style="left:246px;top:752px">
  <svg width="58" height="58" viewBox="0 0 58 58" fill="none" stroke="#0677BA" stroke-width="2.4"><circle cx="29" cy="22" r="10"/><path d="M16 52c0-10 6-16 13-16s13 6 13 16"/><path d="M19 20h20"/><circle cx="44" cy="12" r="5"/></svg>
</div>
<div class="svc-name" style="left:145px;top:883px">Engineering</div>
<p class="svc-text" style="left:160px;top:915px">Lorem ipsum dolor sit amet, consectetur adipiscing elit. In in orci sem. In mattis fermentum pharetra.</p>

<div class="svc-icon" style="left:544px;top:752px">
  <svg width="58" height="58" viewBox="0 0 58 58" fill="none" stroke="#0677BA" stroke-width="2.4"><circle cx="27" cy="31" r="17"/><path d="M10 31h34M27 14c-7 9-7 25 0 34M27 14c7 9 7 25 0 34"/><path d="M40 8c8 0 12 5 12 12-7 0-12-4-12-12z"/></svg>
</div>
<div class="svc-name" style="left:449px;top:883px">Environment</div>
<p class="svc-text" style="left:464px;top:915px">Lorem ipsum dolor sit amet, consectetur adipiscing elit. In in orci sem. In mattis fermentum pharetra.</p>

<div class="svc-icon" style="left:850px;top:752px">
  <svg width="58" height="58" viewBox="0 0 58 58" fill="none" stroke="#0677BA" stroke-width="2.4"><rect x="14" y="8" width="30" height="40" rx="2"/><path d="M20 18h18M20 26h14"/><circle cx="34" cy="38" r="8"/><path d="M40 44l8 8"/></svg>
</div>
<div class="svc-name" style="left:755px;top:883px">Audit &amp; Inspection</div>
<p class="svc-text" style="left:770px;top:915px">Lorem ipsum dolor sit amet, consectetur adipiscing elit. In in orci sem. In mattis fermentum pharetra.</p>

<div class="btn pill" style="left:536px;top:1010px;width:127px;height:42px">Contact Us</div>

<!-- About -->
<section class="abs band" style="top:1143px;height:696px" aria-label="About Us"></section>
<h2 class="section-title serif" style="top:1226px">About Us</h2>
<p class="lead" style="top:1289px">Lorem ipsum dolor sit amet, consectetur adipiscing elit. In in orci sem. In mattis fermentum pharetra. Sed vestibulum maximus risus, et dignissim purus pharetra ac.</p>
<div class="abs" style="left:171px;top:1356px;width:374px;height:374px;border-radius:50%;background:radial-gradient(circle at 45% 40%,#a9b0b6 0%,#6c747c 55%,#3c4248 100%)" role="img" aria-label="Photo of two engineers in yellow hard hats reviewing a clipboard and tablet in a factory"></div>
<p class="abs about-text">Lorem ipsum dolor sit amet, consectetur adipiscing elit. In orci sem. In mattis fermentum pharetra. Sed vestibulum maximus risus, et dignissim purus pharetra ac. Vestibulum efficitur eget sapien at facilisis. Nam sed elit at nulla bibendum imperdiet. Curabitur sollicitudin imperdiet lectus, ac semper nisi viverra eget. Praesent leo turpis, maximus eget erat et.</p>
<div class="btn pill" style="left:597px;top:1546px;width:128px;height:40px">View More</div>
<h3 class="abs serif" style="left:597px;top:1618px;font-size:29px;white-space:nowrap">Lorem Ipsum Dolor Sit Amet</h3>
<div class="chip" style="left:597px;width:104px">Adipiscing elit<br>In in orci sem.</div>
<div class="chip" style="left:710px;width:104px">Adipiscing elit<br>In in orci sem.</div>
<div class="chip" style="left:822px;width:104px">Adipiscing elit<br>In in orci sem.</div>

<!-- Clients -->
<h2 class="section-title serif" style="top:1922px">What Clients Say</h2>
<div class="arrow" style="left:104px;top:2105px">‹</div>
<div class="arrow" style="left:1060px;top:2105px">›</div>
<article class="quote-card" style="left:161px">
  <h3>John Doe</h3>
  <p>Lorem ipsum dolor sit amet, consectetur adipiscing elit. In in orci sem. In mattis fermentum pharetra. Sed vestibulum maximus risus, et dignissim purus pharetra ac. Vestibulum efficitur eget sapien at facilisis. Nam sed elit at nulla bibendum imperdiet et id nulla.</p>
</article>
<article class="quote-card" style="left:614px">
  <h3>Alina R.</h3>
  <p>Lorem ipsum dolor sit amet, consectetur adipiscing elit. In in orci sem. In mattis fermentum pharetra. Sed vestibulum maximus risus, et dignissim purus pharetra ac. Vestibulum efficitur eget sapien at facilisis. Nam sed elit at nulla bibendum imperdiet et id nulla.</p>
</article>

<!-- Why -->
<section class="abs band" style="top:2321px;height:658px" aria-label="Why Work With Us"></section>
<h2 class="abs serif" style="left:161px;top:2390px;font-size:40px">Why Work With Us</h2>
<div class="why-item" style="top:2474px">
  <svg width="62" height="48" viewBox="0 0 62 48" fill="none" stroke="#0677BA" stroke-width="2.2"><circle cx="31" cy="14" r="7"/><circle cx="14" cy="18" r="5"/><circle cx="48" cy="18" r="5"/><path d="M19 44c0-9 5-15 12-15s12 6 12 15M4 40c0-7 4-11 10-11M58 40c0-7-4-11-10-11"/></svg>
  Lorem Ipsum Dolor</div>
<div class="why-item" style="top:2576px">
  <svg width="62" height="50" viewBox="0 0 62 50" fill="none" stroke="#0677BA" stroke-width="2.2"><rect x="16" y="6" width="28" height="38" rx="2"/><path d="M24 6v-3h12v3"/><path d="M22 18l3 3 5-6M33 19h6M22 30l3 3 5-6M33 31h6"/><circle cx="44" cy="38" r="7"/></svg>
  Lorem Ipsum</div>
<div class="why-item" style="top:2679px">
  <svg width="62" height="50" viewBox="0 0 62 50" fill="none" stroke="#0677BA" stroke-width="2.2"><path d="M31 4l17 6v13c0 12-8 20-17 24-9-4-17-12-17-24V10z"/><path d="M23 25l6 6 11-12"/></svg>
  Lorem Sit Ipsum</div>
<div class="why-item" style="top:2782px">
  <svg width="62" height="50" viewBox="0 0 62 50" fill="none" stroke="#0677BA" stroke-width="2.2"><rect x="22" y="4" width="32" height="20" rx="2"/><path d="M28 14h4M36 14h4M44 14h4"/><path d="M12 46V28l8-6 4 4v8h8"/></svg>
  Lorem Ipsum</div>
<div class="abs" style="left:614px;top:2474px;width:424px;height:400px;border-radius:6px;background:linear-gradient(160deg,#b9bec2 0%,#7d858c 45%,#3f464c 100%)" role="img" aria-label="Photo of two engineers in hard hats checking a tablet beside steel machinery"></div>

<!-- Terms -->
<div class="abs doc" role="group" aria-label="Terms and conditions document preview">
  <div class="doc-page">
    <div class="c" style="left:44px;top:12px">14 Harlow Lane<br>Ashgrove, Brisbane QLD<br>T 0400 555 018</div>
    <div class="c" style="left:318px;top:12px">SUMMIT CREST ADVISORY PTY LTD<br>ABN 12 345 678 901<br>ACN 345 678 901</div>
    <div class="c" style="left:455px;top:16px;font-weight:700;font-size:11px;line-height:13px;color:#1a2a5a;display:flex;align-items:center;gap:5px;white-space:nowrap"><span style="width:16px;height:16px;border-radius:50%;background:#1a2a5a;display:inline-block"></span>Summit Crest</div>
    <div class="c" style="left:30px;top:60px;width:250px"><b>1.&nbsp;&nbsp; DEFINITIONS AND INTERPRETATION</b><br><br>&nbsp;&nbsp;&nbsp;&nbsp;<b>1.1.&nbsp; Definitions</b><br>
      <div style="padding-left:26px">In this agreement, unless the context otherwise requires:<br><br><b>Accepted Day Rate</b> means the agreed daily rate for each Employee supplied to the Client, as set out in the Purchase Order.<br><br><b>Accepted Disbursements</b> means approved costs charged in addition to the day rate.<br><br><b>Business Day</b> means a weekday that is not a public holiday.</div></div>
    <div class="c" style="left:318px;top:60px;width:230px"><b>Employee</b> is employed by the Client.<br><br><b>Purchase Order</b> means the order placed by the Client for services.<br><br><b>Standard Terms</b> means these terms of supply.<br><br><b>INTERPRETATION</b><br><br><b>2.1.</b>&nbsp; In this agreement:<br><div style="padding-left:26px">(a)&nbsp; headings are for convenience only;<br>(b)&nbsp; words in the singular include the plural.</div></div>
  </div>
</div>
<div class="abs doc-bar"><span>Page</span><span>1</span><span>/ 10</span><span>—</span><span>+</span></div>
<h2 class="abs terms-title">Terms And Conditions</h2>
<p class="abs terms-text">Lorem ipsum dolor sit amet, consectetur adipiscing elit. In in orci sem. In mattis fermentum pharetra. Sed maximus risus dignissim purus pharetra ac.</p>

<!-- Contact -->
<h2 class="abs contact-title">Contact Us</h2>
<p class="lead" style="top:3541px">Lorem ipsum dolor sit amet, consectetur adipiscing elit. In in orci sem. In mattis fermentum pharetra. Sed vestibulum maximus risus, et dignissim purus pharetra ac.</p>
<form aria-label="Contact form">
  <div class="field" style="top:3624px;height:50px"><svg width="16" height="16" viewBox="0 0 16 16" fill="none" stroke="#555" stroke-width="1.3"><circle cx="8" cy="5" r="3"/><path d="M2 15c0-4 3-6 6-6s6 2 6 6"/></svg>Name<em>*</em></div>
  <div class="field" style="top:3689px;height:50px"><svg width="16" height="16" viewBox="0 0 16 16" fill="none" stroke="#555" stroke-width="1.3"><rect x="1.5" y="3" width="13" height="10" rx="1"/><path d="M2 4l6 5 6-5"/></svg>Email<em>*</em></div>
  <div class="field" style="top:3752px;height:50px"><svg width="16" height="16" viewBox="0 0 16 16" fill="none" stroke="#555" stroke-width="1.3"><path d="M3 2l3 1 1 3-2 1c1 2 2 3 4 4l1-2 3 1 1 3c-6 1-12-5-11-11z"/></svg>Phone</div>
  <div class="field" style="top:3817px;height:105px"><svg width="16" height="16" viewBox="0 0 16 16" fill="none" stroke="#555" stroke-width="1.3"><path d="M2 3h12v8H6l-3 3v-3H2z"/></svg>Message</div>
  <div class="btn pill" style="left:161px;top:3942px;width:121px;height:34px;justify-content:flex-start;padding-left:3px;gap:12px;font-size:12px">
    <span style="width:28px;height:28px;border-radius:50%;background:#fff;display:flex;align-items:center;justify-content:center"><svg width="14" height="12" viewBox="0 0 14 12" fill="none" stroke="#0054AA" stroke-width="1.8"><path d="M1 6h11M7 1l5 5-5 5"/></svg></span>SUBMIT</div>
</form>
<div class="abs map-frame"><div class="map" role="img" aria-label="Street map of the Brisbane office location with a marker"></div></div>

<!-- Footer -->
<footer class="abs site-footer">
  <div class="abs brand" style="left:161px;top:30px;font-size:17px"><span class="brand-dot" style="width:26px;height:26px"></span>Summit Crest Advisory</div>
  <nav class="foot-nav">
    <a style="left:464px">Home</a>
    <a style="left:574px">About Us</a>
    <a style="left:707px">Services</a>
    <a style="left:832px">Industries</a>
    <a style="left:966px">Contact Us</a>
  </nav>
  <div class="rule" style="top:81px"></div>
  <div class="info" style="left:161px">
    <span class="ico"><svg width="16" height="16" viewBox="0 0 16 16" fill="none" stroke="#fff" stroke-width="1.4"><path d="M8 15s5-5 5-9a5 5 0 0 0-10 0c0 4 5 9 5 9z"/><circle cx="8" cy="6" r="1.8"/></svg></span>
    <div>123 Building Name, Street Name,<br>City Name, State XY-123456</div></div>
  <div class="info" style="left:528px">
    <span class="ico"><svg width="16" height="16" viewBox="0 0 16 16" fill="none" stroke="#fff" stroke-width="1.4"><path d="M3 2l3 1 1 3-2 1c1 2 2 3 4 4l1-2 3 1 1 3c-6 1-12-5-11-11z"/></svg></span>
    <div><b>Phone</b><br>123 456 7890</div></div>
  <div class="info" style="left:792px">
    <span class="ico"><svg width="16" height="16" viewBox="0 0 16 16" fill="none" stroke="#fff" stroke-width="1.4"><rect x="1.5" y="3" width="13" height="10" rx="1"/><path d="M2 4l6 5 6-5"/></svg></span>
    <div><b>Email</b><br>info@scadvisoryhub.com</div></div>
  <div class="rule" style="top:166px"></div>
  <div class="abs" style="left:161px;top:200px;font-size:12px">© 2023 &nbsp;<b style="font-weight:600">Summit Crest Advisory.</b> All Rights Reserved.</div>
  <a class="abs" style="left:1008px;top:192px;width:30px;height:30px;border-radius:50%;border:1.5px solid #fff" aria-label="WorkCircle"></a>
</footer>

</body>
</html>
```